Bright and beautiful business card for a coach

I'm a personal and business coach based in Perth, Australia. I need a business card that whilst subtle and elegant, will stand out and appeal on a table full of cards.

My business name is Tide Mentoring and the business card must represent the warmth and brightness implied in the name, without being gimmicky. It must have a warmth and appeal and be easy to read.

I prefer clean, minimalist designs.

It must align with the feel of my website and socials: https://www.tidementoring.com.au/
https://www.instagram.com/tidementoringau/
https://www.facebook.com/tidementoringau
Updates

Hi Designers Thank you so much for taking the time to submit designs. I wonder if I could have explained myself a little better. Most of the designs that have been submitted look rather formal and many have quite corporate looking embellishments on them (to my eye). I would like softer, warmer, more organic. I’m open to people playing about and being more abstract, using softer embellishments (e.g the line drawing flowers and grasses I’ve used in my socials) incorporating other colours from my palette or like the social icons in my email signature (in PDF), perhaps playing with size/oversize, playing with the bleed. Please don’t be constrained by what I’ve already done, it merely needs to compliment. I’m sorry if I’m not using the right words or have led you astray. I’m no designer, but I’ve done my website, socials, email signature etc all myself (my logo was a design contest) and I was really hoping for my business card to be something more creative than I could have made with a template. Reminder: No black cards/sides please. Thank you 😊

Target Market(s)

Individuals, most likely but not all female. Creative thinkers. Likely professionals.

Industry/Entity Type

Business & Personal Coach

Contact Information for Business Card

(Tide Mentoring Logo) Name: Maren Delsby; Title: Business & Personal Coach; Phone number: +61 (0)438 915307; Email: maren@tidementoring.com.au; Website: https://tidementoring.com.au; Social icons for Facebook, Instagram & LinkedIn: @tidementoringAU. Optional strapline: "A thinking partner to help you cut through the noise"

Font styles to use
Sans Serif

Colors
00AB8E
00BBA5
67D7C9
C6EFE9
E9F9F6
59FF00
82FF00
B8FF75
E3FFCB
F4FFEA
FFC000
F8CF3A
FAE287
FDF2CF
FEFAEE

Requirements
Must have
• Must align with feel of my website and socials. Must have a pop of #FFC000 (possibly whole of one side, or at least a block). Bright or white background. Easy to read.
Nice to have
• Possibly incorporate the sunshine/grass picture I have used in website and socials - will upload.
Should not have
• Must not be black or dark. Not impersonal or corporate looking.

```html
<!DOCTYPE html>
<html lang="en">
<head>
<meta charset="utf-8">
<title>Tide Mentoring — Business Card Front</title>
<link rel="stylesheet" href="https://fonts.googleapis.com/css2?family=Lato:wght@300;400&display=swap">
<style>
  :root {
    --sun: #FFC000;
    --sun-band: #FFD22E;
    --sun-soft: #F8CF3A;
    --sun-pale: #FAE287;
    --cream: #FDF2CF;
    --ivory: #FEFAEE;
    --sand: #F3E6C8;
    --white: #FFFFFF;
    --ink-warm: #7A4E0C;
  }
  * { margin: 0; padding: 0; box-sizing: border-box; }
  html, body {
    width: 1200px;
    height: 733px;
    overflow: hidden;
    background: var(--sun);
  }
  .card {
    position: relative;
    width: 1200px;
    height: 733px;
    overflow: hidden;
    background: var(--sun);
    font-family: "Lato", sans-serif;
  }
  .card__pattern {
    position: absolute;
    inset: 0;
    background: var(--sun);
  }
  .card__waves {
    position: absolute;
    inset: 0;
    width: 1200px;
    height: 733px;
  }
  .brand {
    position: absolute;
    left: 0;
    right: 0;
    top: 352px;
    text-align: center;
    display: flex;
    justify-content: center;
    align-items: center;
    gap: 22px;
  }
  .brand__mark {
    width: 14px;
    height: 14px;
    border-radius: 50%;
    background: var(--white);
  }
  .brand__name {
    font-family: "Lato", sans-serif;
    font-weight: 300;
    font-size: 62px;
    letter-spacing: 0.16em;
    text-transform: uppercase;
    color: var(--white);
    line-height: 1;
  }
  .card__url {
    position: absolute;
    left: 0;
    right: 0;
    top: 642px;
    text-align: center;
    font-family: "Lato", sans-serif;
    font-weight: 300;
    font-size: 31px;
    letter-spacing: 0.02em;
    color: var(--ink-warm);
  }
</style>
</head>
<body>
  <main class="card">
    <div class="card__pattern" role="img" aria-label="Scattered soft petal pattern in deeper sunshine yellow"></div>

    <svg class="card__waves" viewBox="0 0 1200 733" aria-hidden="true">
      <!-- top right sweep -->
      <path d="M757,0 C815,120 975,222 1200,200 L1200,0 Z" fill="var(--sun-band)"/>
      <path d="M805,0 C880,80 1030,145 1200,158 L1200,0 Z" fill="var(--sun-soft)"/>
      <path d="M900,0 C980,60 1090,120 1200,150 L1200,0 Z" fill="var(--sun-pale)"/>
      <path d="M1010,0 C1080,45 1150,100 1200,150 L1200,0 Z" fill="var(--cream)"/>
      <path d="M1085,0 C1130,35 1175,75 1200,105 L1200,0 Z" fill="var(--ivory)"/>

      <!-- bottom left sweep -->
      <path d="M0,205 C220,262 405,510 478,733 L0,733 Z" fill="var(--sun-band)"/>
      <path d="M0,345 C155,420 295,590 355,733 L0,733 Z" fill="var(--sun-pale)"/>
      <path d="M0,478 C150,525 305,640 405,733 L0,733 Z" fill="var(--sand)"/>
      <path d="M0,525 C140,570 275,650 345,733 L0,733 Z" fill="var(--ivory)"/>
      <path d="M0,600 C120,640 230,690 285,733 L0,733 Z" fill="var(--cream)"/>
      <path d="M0,655 C80,680 150,705 190,733 L0,733 Z" fill="var(--sun-pale)"/>
    </svg>

    <div class="brand">
      <span class="brand__mark"></span>
      <span class="brand__name">Tide Mentoring</span>
    </div>

    <p class="card__url">www.tidementoring.com.au</p>
  </main>
</body>
</html>
```